Criação de Projeto Combo top of mind para Logística, Entrega & Armazenamento
A empresa queria:
" OFERECEMOS SERVIÇOS LOGISTICA COM TRANSPORTE DE CARGAS PESADAS, CARGAS FRACIONADAS E TRANSPORTE EXECUTIVO DE PASSAGEIROS E FRETAMENTO COM ONIBUS, VANS E MMICRO ONIBUS "

```html
<!DOCTYPE html>
<html lang="pt-BR">
<head>
<meta charset="utf-8">
<title>Nortevia – Cartão de Visita</title>
<link href="https://fonts.googleapis.com/css2?family=Montserrat:wght@400;500;800&display=swap" rel="stylesheet">
<style>
  :root {
    --bg: #e9e6e1;
    --card-white: #ffffff;
    --card-black: #151515;
    --brand-yellow: #f6bd16;
    --text-light: #ffffff;
    --text-dark: #151515;
  }
  * { margin: 0; padding: 0; box-sizing: border-box; }
  html, body {
    width: 1200px; height: 1200px; overflow: hidden;
    background: var(--bg);
    font-family: "Montserrat", Arial, sans-serif;
  }
  .business-card {
    position: absolute;
    left: 60px; top: 440px;
    width: 1080px; height: 320px;
    border-radius: 18px;
    overflow: hidden;
    box-shadow: 0 10px 30px rgba(0,0,0,0.18);
  }
  .card-shapes { position: absolute; inset: 0; }
  .brand {
    position: absolute;
    left: 48px; top: 0; width: 380px; height: 320px;
    display: flex; align-items: center; gap: 14px;
  }
  .brand-dot {
    flex: 0 0 36px;
    width: 36px; height: 36px; border-radius: 50%;
    background: var(--brand-yellow);
  }
  .brand-name {
    font-weight: 800; font-size: 46px; letter-spacing: 1px;
    color: var(--text-dark); text-transform: uppercase;
    white-space: nowrap;
  }
  .contact-block {
    position: absolute; left: 572px; top: 22px;
    color: var(--text-light);
  }
  .person-name {
    color: var(--brand-yellow); font-weight: 500; font-size: 31px; line-height: 38px;
  }
  .person-role { font-size: 21px; line-height: 28px; margin-bottom: 18px; }
  .contact-list { list-style: none; }
  .contact-item {
    display: flex; align-items: flex-start; gap: 16px;
    font-size: 21px; line-height: 26px; margin-bottom: 16px;
  }
  .contact-item svg { flex: 0 0 22px; width: 22px; height: 22px; margin-top: 2px; }
</style>
</head>
<body>
  <div class="business-card">
    <svg class="card-shapes" viewBox="0 0 1080 320" width="1080" height="320" aria-hidden="true">
      <rect width="1080" height="320" fill="var(--card-white)"/>
      <path d="M485 0 C455 90 448 200 470 320 L1080 320 L1080 0 Z" fill="var(--brand-yellow)"/>
      <path d="M540 0 C505 90 498 200 520 320 L1080 320 L1080 0 Z" fill="var(--card-black)"/>
    </svg>

    <div class="brand">
      <span class="brand-dot"></span>
      <span class="brand-name">Nortevia</span>
    </div>

    <div class="contact-block">
      <p class="person-name">Nome Completo</p>
      <p class="person-role">Cargo ou Função</p>
      <ul class="contact-list">
        <li class="contact-item">
          <svg viewBox="0 0 24 24"><path fill="var(--brand-yellow)" d="M6.6 10.8a15 15 0 0 0 6.6 6.6l2.2-2.2c.3-.3.7-.4 1-.2 1.1.4 2.3.6 3.6.6.6 0 1 .4 1 1V20c0 .6-.4 1-1 1A17 17 0 0 1 3 4c0-.6.4-1 1-1h3.5c.6 0 1 .4 1 1 0 1.3.2 2.5.6 3.6.1.3 0 .7-.2 1z"/></svg>
          <span>(00) 0000-0000</span>
        </li>
        <li class="contact-item">
          <svg viewBox="0 0 24 24"><rect x="2" y="5" width="20" height="14" rx="1.5" fill="var(--brand-yellow)"/><path d="M3 6l9 7 9-7" fill="none" stroke="var(--card-black)" stroke-width="1.8"/></svg>
          <span>contato@seusite.com.br</span>
        </li>
        <li class="contact-item">
          <svg viewBox="0 0 24 24" fill="none" stroke="var(--brand-yellow)" stroke-width="2"><circle cx="12" cy="12" r="9.5" fill="var(--brand-yellow)"/><path stroke="var(--card-black)" stroke-width="1.4" d="M2.5 12h19M12 2.5c3 3 3 16 0 19M12 2.5c-3 3-3 16 0 19"/></svg>
          <span>www.nortevia.com.br</span>
        </li>
        <li class="contact-item">
          <svg viewBox="0 0 24 24"><path fill="var(--brand-yellow)" d="M12 2a7 7 0 0 0-7 7c0 5.3 7 13 7 13s7-7.7 7-13a7 7 0 0 0-7-7zm0 9.5A2.5 2.5 0 1 1 12 6.5a2.5 2.5 0 0 1 0 5z"/></svg>
          <span>Nome da Rua, 00 - Bairro<br>Cidade/UF - Cep: 00.000-000</span>
        </li>
      </ul>
    </div>
  </div>
</body>
</html>
```